Upmarket Bathroom and Kitchen ware supplier needs a classy business card design

We are a company based in Fiji, we sell plumbing ware (Kitchen and bathroom taps, Basins,showers, toilets etc) through up market show rooms to individuals and directly through Architects and designers of resorts and holiday houses for new builds and renovations. we are wanting to upgrade our over all look and brand. we are starting with a new logo but will be rebranding the whole business. This project is for a business card design for my management and tales team I would like it to be dark, classy and interesting

Target Market(s)

Resort directors and Management, High end holiday home owners

Contact Information for Business Card

Neil Dawson
Director
+64219473815

Colors

Designer to choose colors to be used in the design.

Requirements
Must have
• Must have an upmarket appearance I like darker charcoal shades but will be guided by the designers
• Please any catch phrases like "Crafting remarkable living rooms" this belongs tpo one of our suppliers so can not be used.
Nice to have
• Double sided, so front dedicated to logo provided and back info about the business and the person.

```html
<!DOCTYPE html>
<html lang="en">
<head>
<meta charset="utf-8">
<title>Meridian Interiors — Business Card</title>
<link href="https://fonts.googleapis.com/css2?family=Lato:wght@300;400;700&display=swap" rel="stylesheet">
<style>
  :root {
    --backdrop: #2a2a2a;
    --card: #050505;
    --card-edge: #161616;
    --ink-white: #ffffff;
    --ink-muted: #4a5145;
    --pattern-a: #0a0a0a;
    --pattern-b: #1a1a1a;
  }
  * { margin: 0; padding: 0; box-sizing: border-box; }
  html, body {
    width: 1200px;
    height: 1108px;
    overflow: hidden;
    background: var(--backdrop);
    font-family: "Lato", Arial, sans-serif;
  }
  .sheet {
    position: relative;
    width: 1200px;
    height: 1108px;
    display: flex;
    justify-content: center;
    align-items: center;
    gap: 56px;
  }
  .card {
    position: relative;
    width: 400px;
    height: 620px;
    background: var(--card);
    border-radius: 22px;
    border: 1px solid var(--card-edge);
    box-shadow: 0 24px 50px rgba(0,0,0,0.55);
    overflow: hidden;
    color: var(--ink-white);
  }
  .wordmark {
    position: absolute;
    left: 0;
    right: 0;
    text-align: center;
    font-weight: 300;
    color: var(--ink-white);
    line-height: 1.5;
  }
  .wordmark__name {
    display: block;
    font-size: 30px;
    letter-spacing: 12px;
    text-indent: 12px;
    text-transform: uppercase;
  }
  .wordmark__sub {
    display: block;
    font-size: 11px;
    letter-spacing: 6px;
    text-indent: 6px;
    text-transform: uppercase;
  }
  .card--front .wordmark { top: 210px; }
  .person {
    position: absolute;
    left: 44px;
    top: 390px;
  }
  .person__name {
    font-size: 34px;
    font-weight: 700;
    letter-spacing: -0.5px;
  }
  .person__role {
    margin-top: 2px;
    font-size: 19px;
    font-weight: 400;
    color: var(--ink-muted);
  }
  .person__phone {
    margin-top: 26px;
    display: flex;
    align-items: center;
    gap: 14px;
    font-size: 17px;
    color: var(--ink-muted);
    letter-spacing: 0.5px;
  }
  .person__phone svg { width: 16px; height: 16px; }
  .card__pattern {
    position: absolute;
    inset: 0;
    background: linear-gradient(150deg, var(--pattern-b) 0%, var(--pattern-a) 70%, var(--card) 100%);
  }
  .card--back .wordmark { bottom: 70px; }
</style>
</head>
<body>
  <main class="sheet">
    <section class="card card--front" aria-label="Card front">
      <div class="wordmark">
        <span class="wordmark__name">Meridian</span>
        <span class="wordmark__sub">Interiors</span>
      </div>
      <div class="person">
        <h1 class="person__name">Neil Dawson</h1>
        <p class="person__role">Director</p>
        <p class="person__phone">
          <svg viewBox="0 0 24 24" aria-hidden="true"><path fill="#ffffff" d="M6.6 10.8a15.1 15.1 0 0 0 6.6 6.6l2.2-2.2a1 1 0 0 1 1-.25 11.4 11.4 0 0 0 3.6.57 1 1 0 0 1 1 1V20a1 1 0 0 1-1 1A17 17 0 0 1 3 4a1 1 0 0 1 1-1h3.5a1 1 0 0 1 1 1c0 1.25.2 2.45.57 3.57a1 1 0 0 1-.25 1z"/></svg>
          +64219473815
        </p>
      </div>
    </section>

    <section class="card card--back" aria-label="Card back">
      <div class="card__pattern" role="img" aria-label="Faint repeating brand pattern across the card back"></div>
      <div class="wordmark">
        <span class="wordmark__name">Meridian</span>
        <span class="wordmark__sub">Interiors</span>
      </div>
    </section>
  </main>
</body>
</html>
```